Simple AD for Digital Publication

Total Size 5" x 5", may include boarder or not
Image Provided; crop or use as background
Incorporate Logo and text as provided

Target Market(s)

Sound Contractors / Integrators

Industry/Entity Type

Audio Video Lighting

Requirements
Must have
• Bold Look that reflects our brand. see website: tovermundic.com - cohesive text and style

```html
<!DOCTYPE html>
<html lang="en">
<head>
<meta charset="utf-8">
<title>Tovermundic Co — Become a Dealer</title>
<link href="https://fonts.googleapis.com/css2?family=Oswald:wght@600;700&family=Montserrat:ital,wght@0,700;0,800;1,800&family=Roboto:ital,wght@1,700&display=swap" rel="stylesheet">
<style>
  :root {
    --brand-red: #b01e23;
    --brand-red-dark: #8e1519;
    --ink: #1f1f1f;
    --graphite: #3b3b3d;
    --paper: #ffffff;
    --backdrop: #e4e4e4;
  }
  * { margin: 0; padding: 0; box-sizing: border-box; }
  html, body {
    width: 1200px; height: 1036px; overflow: hidden;
    background: var(--backdrop);
  }
  .ad {
    position: absolute; left: 82px; top: 0;
    width: 1036px; height: 1036px;
    background: var(--paper);
    overflow: hidden;
  }
  .dealer-bar {
    position: absolute; left: 62px; top: 730px;
    width: 700px; height: 80px;
    background: var(--ink);
    z-index: 0;
  }
  .feature-diamond {
    position: absolute; inset: 0;
    width: 1036px; height: 1036px;
    z-index: 1;
  }
  .content { position: absolute; inset: 0; z-index: 2; }

  .brand { position: absolute; left: 62px; top: 62px; display: flex; align-items: flex-start; gap: 22px; }
  .brand-square { width: 84px; height: 84px; background: var(--brand-red); margin-top: 8px; }
  .brand-name {
    font-family: "Oswald", sans-serif; font-weight: 700;
    font-size: 66px; line-height: 70px; color: var(--graphite);
    letter-spacing: -0.5px; text-transform: uppercase;
  }
  .brand-tagline {
    font-family: "Roboto", sans-serif; font-style: italic; font-weight: 700;
    font-size: 29px; color: var(--graphite);
  }

  .headline {
    position: absolute; left: 60px; top: 204px;
    font-family: "Oswald", sans-serif; font-weight: 700;
    font-size: 130px; line-height: 128px;
    color: var(--brand-red); text-transform: uppercase;
    letter-spacing: -1px;
  }
  .subhead {
    position: absolute; left: 62px; top: 466px;
    font-family: "Montserrat", sans-serif; font-style: italic; font-weight: 800;
    font-size: 66px; line-height: 70px; color: var(--ink);
    text-transform: uppercase; letter-spacing: -1px;
  }
  .subhead-accent {
    position: absolute; left: 60px; top: 604px;
    font-family: "Oswald", sans-serif; font-weight: 600;
    font-size: 94px; line-height: 116px;
    color: var(--brand-red); text-transform: uppercase;
    letter-spacing: -4px;
  }
  .dealer-label {
    position: absolute; left: 80px; top: 730px; height: 80px;
    display: flex; align-items: center;
    font-family: "Montserrat", sans-serif; font-weight: 800;
    font-size: 52px; color: var(--paper); letter-spacing: -0.5px;
  }
  .cta {
    position: absolute; left: 55px; top: 844px;
    width: 370px; height: 74px;
    text-decoration: none;
  }
  .cta-pill {
    position: absolute; left: 0; top: 2px; width: 330px; height: 70px;
    background: var(--brand-red);
    border: 3px solid var(--brand-red-dark);
    border-radius: 35px;
    display: flex; align-items: center; padding-left: 34px;
    font-family: "Montserrat", sans-serif; font-weight: 800;
    font-size: 33px; color: var(--paper);
  }
  .cta-icon { position: absolute; left: 282px; top: -6px; width: 86px; height: 86px; }
</style>
</head>
<body>
  <main class="ad">
    <div class="dealer-bar"></div>

    <svg class="feature-diamond" viewBox="0 0 1036 1036">
      <defs>
        <linearGradient id="photoTone" x1="0" y1="0" x2="0" y2="1">
          <stop offset="0" stop-color="#1c2432"/>
          <stop offset="0.32" stop-color="#3a3a22"/>
          <stop offset="0.5" stop-color="#6b6a3a"/>
          <stop offset="0.66" stop-color="#9a7a62"/>
          <stop offset="0.82" stop-color="#7e6552"/>
          <stop offset="1" stop-color="#a58a74"/>
        </linearGradient>
      </defs>
      <polygon points="958,72 1448,562 958,1052 468,562" fill="var(--brand-red)"/>
      <polygon points="958,92 1428,562 958,1032 488,562" fill="url(#photoTone)"
               role="img" aria-label="Photo of a stage floor pocket with cables running out beside string lights and greenery"/>
    </svg>

    <div class="content">
      <div class="brand">
        <div class="brand-square"></div>
        <div>
          <div class="brand-name">Tovermundic Co</div>
          <div class="brand-tagline">Stage Pocket Systems Connectivity</div>
        </div>
      </div>

      <h1 class="headline">Protect &amp;<br>Conceal</h1>
      <p class="subhead">High &amp; Low<br>Voltage</p>
      <p class="subhead-accent">Connectivity</p>

      <p class="dealer-label">BECOME A DEALER</p>

      <a class="cta" href="https://tovermundic.com">
        <span class="cta-pill">CLICK HERE</span>
        <svg class="cta-icon" viewBox="0 0 86 86">
          <circle cx="43" cy="43" r="40" fill="var(--brand-red)" stroke="var(--brand-red-dark)" stroke-width="3"/>
          <circle cx="43" cy="43" r="33" fill="none" stroke="#fff" stroke-width="2.5"/>
          <path d="M34 22 a9 9 0 0 1 18 0" fill="none" stroke="#fff" stroke-width="2.5" stroke-linecap="round"/>
          <path d="M39 24 q0-4 4-4 q4 0 4 4 v14 l3-1 q4 0 4 4 l4 0 q4 0 4 4 v10 q0 10-10 12 h-7 q-6 0-9-6 l-7-10 q-2-4 2-5 q3 0 5 3 l3 3 z" fill="#fff"/>
        </svg>
      </a>
    </div>
  </main>
</body>
</html>
```